Business Card Design Project

I want a cleaner business card and envelope then what we have now, its too crowded.
Updates

I update with logo, this can be changed anyway you feel it looks best. I also have put gaurantee on there and extended time, this is my first time doing this. Also gave an example of current card

Target Market(s)

a wide array of customers from lattice 700 to small companies and cleints

Industry/Entity Type

Business

Requirements
Must have
• Need to have address, telephone number email
Nice to have
• a sharp professional card that stands out but is still very clean.
Should not have
• Not crazy looking

```html
<!DOCTYPE html>
<html lang="en">
<head>
<meta charset="utf-8">
<title>Harbor Point Insurance Group – Envelope and Business Card</title>
<link rel="stylesheet" href="https://fonts.googleapis.com/css2?family=Arimo:ital,wght@0,400;0,700;1,400&display=swap">
<style>
  :root {
    --page: #ffffff;
    --paper: #ffffff;
    --ink: #111111;
    --edge: #3a3a3a;
    --mark: #8a8a8a;
    --rule: #555555;
  }
  html, body {
    margin: 0;
    padding: 0;
    background: var(--page);
    overflow: hidden;
  }
  .canvas {
    position: relative;
    width: 1200px;
    height: 537px;
    overflow: hidden;
    font-family: "Arimo", Arial, sans-serif;
    color: var(--ink);
  }

  /* Shared brand block: plain square beside the company name */
  .brand {
    position: absolute;
    display: flex;
    flex-direction: row;
    align-items: center;
    gap: 8px;
  }
  .brand-square {
    flex: none;
    background: var(--mark);
  }
  .brand-name {
    margin: 0;
    font-weight: 400;
    color: var(--ink);
  }
  .company {
    font-weight: 700;
    margin: 0 0 4px;
  }
  .address {
    margin: 0;
    font-style: normal;
  }

  /* Envelope */
  .envelope {
    position: absolute;
    left: 44px;
    top: 32px;
    width: 828px;
    height: 468px;
    background: var(--paper);
    border: 1px solid var(--edge);
    box-sizing: border-box;
  }
  .envelope .brand {
    left: 22px;
    top: 42px;
  }
  .envelope .brand-square {
    width: 36px;
    height: 36px;
  }
  .envelope .brand-name {
    font-size: 12px;
    line-height: 15px;
  }
  .envelope .divider {
    position: absolute;
    left: 169px;
    top: 24px;
    width: 1px;
    height: 75px;
    background: var(--rule);
  }
  .envelope .return-address {
    position: absolute;
    left: 186px;
    top: 30px;
    font-size: 11px;
    line-height: 14px;
  }

  /* Business card */
  .card {
    position: absolute;
    left: 625px;
    top: 115px;
    width: 520px;
    height: 290px;
    background: var(--paper);
    border: 1px solid var(--edge);
    box-sizing: border-box;
  }
  .card .brand {
    left: 16px;
    top: 36px;
  }
  .card .brand-square {
    width: 30px;
    height: 30px;
  }
  .card .brand-name {
    font-size: 11px;
    line-height: 14px;
  }
  .card .person {
    position: absolute;
    left: 140px;
    top: 100px;
    width: 300px;
    text-align: center;
  }
  .card .person-name {
    font-size: 24px;
    font-weight: 700;
    margin: 0;
  }
  .card .person-title {
    font-size: 18px;
    font-style: italic;
    margin: 4px 0 0;
  }
  .card .office {
    position: absolute;
    left: 28px;
    top: 210px;
    font-size: 11px;
    line-height: 14px;
  }
  .card .contact {
    position: absolute;
    left: 262px;
    top: 198px;
    font-size: 11px;
    line-height: 16px;
    margin: 0;
    display: grid;
    grid-template-columns: auto auto;
    column-gap: 6px;
  }
  .card .contact dt { font-weight: 700; }
  .card .contact dd { margin: 0; }
  .card .contact a { color: var(--ink); }
</style>
</head>
<body>
<div class="canvas">

  <section class="envelope" aria-label="Envelope">
    <div class="brand">
      <div class="brand-square" aria-hidden="true"></div>
      <p class="brand-name">Harbor Point<br>Insurance Group</p>
    </div>
    <div class="divider" aria-hidden="true"></div>
    <div class="return-address">
      <p class="company">Harbor Point Insurance Group</p>
      <address class="address">18230 Maple Crest Ave.<br>Oakridge Falls,<br>MI 48900</address>
    </div>
  </section>

  <section class="card" aria-label="Business card">
    <div class="brand">
      <div class="brand-square" aria-hidden="true"></div>
      <p class="brand-name">Harbor Point<br>Insurance Group</p>
    </div>
    <div class="person">
      <h1 class="person-name">Marla Quint-Hoyle</h1>
      <p class="person-title">Operations Manager</p>
    </div>
    <div class="office">
      <p class="company">Harbor Point Insurance Group</p>
      <address class="address">18230 Maple Crest Ave.<br>Oakridge Falls,<br>MI 48900</address>
    </div>
    <dl class="contact">
      <dt>Email:</dt>
      <dd><a href="mailto:mquint-hoyle@harborpointagency.com">mquint-hoyle@harborpointagency.com</a></dd>
      <dt>Mobile:</dt>
      <dd>555-204-3100 ext 232</dd>
    </dl>
  </section>

</div>
</body>
</html>
```